Electrictrian Contractor Website Design

We are working with an electrical contractor in California called Crest Electric.

Some sites to use for content/competitors and inspiration:
https://tamrinwired.com
https://pravikdesk.surf/web/contractor/ (lots of contractor website designs we've approved and continue to show clients)

Thank you for taking the time to consider designing a website for us. We are web developers based in Stockton, CA, USA. Most of our projects go through the same process. Understanding this process may help you win a project with us. We custom-code all of our websites in-house. We don’t have any requirements as to what tools you use for your design, but we prefer Figma files. For any design that we label as four-stars, we send it to the client for review. The client picks the final design they want us to use. Once we complete this process, we will continue to show additional clients all the four-star sites and purchase them later. Your designs will have multiple chances to sell. For better chances of success, we ask that you follow these guidelines.

IMAGES:
If you use any images or icons in the design, we ask that you have a link to the asset so we can purchase the image/icon. Most of the designs we submit do not have the customer’s images on them unless they have some great images. Be creative; show us the feeling you are trying to portray with your image choices. Use any royalty-free site you choose. We subscribe to Quillo and mainly use their images, but we can purchase images outside of Quillo.

PLEASE NOTE: we will not submit designs to clients with watermarks on the images.

FONTS:
We ask that you identify the fonts used in the design. This can be done in a message if you want. We typically use Google Fonts and Quillo Fonts.

CONTENT:
We're always open to different content and ideas. We often submit designs with stock images so the client can see our vision. We typically take pictures after the website launch to use their images with our vision. Lorem Ipsum is fine for paragraphs, but we ask that you write the headers in correct English. We want to be able to show the vision and identify the sections of the website.

INSPIRATION:
We typically add a couple of links in the brief of websites we like to help you get started in your design.

REVISIONS:
We do not often ask for revisions of the designs unless we see something in the design that may not appeal to the client. If there are slight changes that we want to make, we do that in the development process.

FEEDBACK:
We rarely give feedback on designs during the design process. We are working on many website projects and do not have the time to provide feedback. We usually respond if your request is well thought out and asks specific questions, but a note asking “feedback, please” usually goes unanswered

```html
<!DOCTYPE html>
<html lang="en">
<head>
<meta charset="utf-8">
<title>Crest Electric — Electrical Contractor</title>
<link href="https://fonts.googleapis.com/css2?family=Montserrat:wght@400;500;600;700;800&family=Poppins:wght@400;500;600&display=swap" rel="stylesheet">
<style>
:root{
  --navy:#0d3d8c;
  --navy-dark:#0a2f6e;
  --yellow:#f5b400;
  --yellow-deep:#e9a800;
  --ink:#1d1d1f;
  --text:#333;
  --muted:#555;
  --white:#fff;
  --black:#050505;
  --soft:#f3f4f6;
}
*{margin:0;padding:0;box-sizing:border-box}
html,body{width:1200px;height:3915px;overflow:hidden}
body{position:relative;background:var(--white);font-family:"Poppins",sans-serif;color:var(--text)}
.abs{position:absolute}
.heading{font-family:"Montserrat",sans-serif}

/* header */
.topbar{left:350px;top:0;width:775px;height:46px;background:var(--navy);clip-path:polygon(0 0,100% 0,96.5% 100%,3.5% 100%)}
.topbar-item{top:12px;color:var(--white);font-size:15px;display:flex;align-items:center;gap:10px;font-family:"Poppins",sans-serif}
.login{left:909px;top:9px;width:111px;height:29px;border-radius:15px;background:var(--white);color:var(--yellow);font-size:15px;font-weight:600;display:flex;align-items:center;justify-content:center;gap:6px}
.brand{left:108px;top:16px;width:190px;text-align:center;font-family:"Montserrat",sans-serif;font-weight:600;color:var(--navy);line-height:1.05}
.brand .l1{font-size:30px;letter-spacing:12px;padding-left:12px;display:block}
.brand .l2{font-size:30px;letter-spacing:6px;padding-left:6px;display:block}
.nav{font-family:"Montserrat",sans-serif;font-size:16px;font-weight:500;color:var(--ink)}
.nav a{color:inherit;text-decoration:none;position:absolute;white-space:nowrap}
.nav .active{color:var(--yellow)}
.nav .active::after{content:"";position:absolute;left:0;right:0;top:27px;height:4px;background:var(--yellow)}

/* hero */
.hero-photo{left:0;top:97px;width:1200px;height:633px;background:linear-gradient(100deg,#17233a 0%,#243247 38%,#3a3d43 55%,#b8612a 72%,#1f2b44 92%)}
.hero-shade{left:0;top:97px;width:1200px;height:633px;background:linear-gradient(90deg,rgba(10,18,34,.75) 0%,rgba(10,18,34,.35) 45%,rgba(0,0,0,0) 70%)}
.hero-kicker{left:111px;top:256px;color:var(--yellow);font-size:33px;font-weight:500;letter-spacing:1px}
.hero-title{left:106px;top:302px;color:var(--white);font-size:63px;font-weight:400;letter-spacing:1px;white-space:nowrap}
.hero-title b{font-weight:800}
.hero-text{left:111px;top:382px;width:420px;color:var(--white);font-size:14.5px;line-height:31px;font-weight:500}
.btn{display:flex;align-items:center;justify-content:center;font-family:"Montserrat",sans-serif;font-weight:700;font-size:16px;border-radius:24px;text-transform:uppercase}
.btn-yellow{background:var(--yellow);color:var(--white)}
.btn-navy{background:var(--navy);color:var(--white)}

/* stats */
.stat{top:808px;width:230px;text-align:center}
.stat .num{font-family:"Montserrat",sans-serif;font-size:44px;font-weight:600;color:var(--navy);line-height:1}
.stat .lbl{font-family:"Montserrat",sans-serif;font-size:16px;font-weight:600;color:var(--ink);margin-top:18px}
.stat-rule{top:814px;width:5px;height:68px;background:var(--yellow)}

/* about */
.about-ring{left:122px;top:968px;width:434px;height:434px;border-radius:50%;background:#dfe4ec}
.about-photo{left:136px;top:982px;width:406px;height:406px;border-radius:50%;background:linear-gradient(180deg,#8fbde6 0%,#c9dcea 45%,#e49a3a 70%,#5d6b80 100%)}
.section-title{font-family:"Montserrat",sans-serif;font-size:33px;color:var(--ink);font-weight:400;white-space:nowrap}
.section-title b{font-weight:700}
.about-title{left:631px;top:973px}
.about-rule{left:631px;top:1024px;width:52px;height:4px;background:var(--yellow)}
.about-text{left:631px;top:1043px;width:455px;height:282px;overflow:hidden;font-size:13px;line-height:31px;color:var(--text)}

/* services */
.services-band{left:0;top:1420px;width:1200px;height:750px}
.center-title{left:0;width:1200px;text-align:center}
.services-title{top:1556px;color:var(--white)}
.services-rule{left:574px;top:1604px;width:52px;height:4px;background:var(--white)}
.service-card{top:1714px;width:303px;height:279px;text-align:center}
.service-card.featured{background:var(--white);border-radius:12px}
.service-icon{top:1663px;width:92px;height:92px;border-radius:50%;display:flex;align-items:center;justify-content:center}
.service-name{font-family:"Montserrat",sans-serif;font-size:20px;font-weight:700;margin-top:58px}
.service-text{font-size:14px;line-height:31px;margin-top:8px;padding:0 10px}
.service-link{font-family:"Montserrat",sans-serif;font-size:15.5px;font-weight:700;margin-top:10px}
.on-yellow{color:var(--white)}
.on-white .service-name,.on-white .service-link{color:var(--navy)}
.on-white .service-text{color:var(--text)}
.arrow{width:28px;height:28px}

/* projects */
.projects-title{top:2201px}
.projects-title,.projects-title b{color:var(--navy)}
.projects-rule{left:574px;top:2254px;width:52px;height:4px;background:var(--navy)}
.project{top:2288px;width:309px;height:311px}

/* testimonials */
.testi-band{left:0;top:2746px;width:1200px;height:290px;background:linear-gradient(90deg,#1b4fa6 0%,#1e56ad 50%,#2a63b7 100%)}
.testi-title{top:2846px;color:var(--white)}
.testi-card{top:2925px;width:306px;height:327px;background:var(--white);border-radius:8px;box-shadow:0 6px 18px rgba(0,0,0,.12);padding:24px 24px}
.stars{color:var(--yellow);font-size:16px;letter-spacing:2px;line-height:1}
.testi-text{font-size:13px;line-height:25.6px;color:var(--ink);margin-top:10px;text-align:justify;font-family:"Poppins",sans-serif;height:128px;overflow:hidden}
.testi-rule{position:absolute;left:24px;right:24px;top:216px;height:1px;background:#9aa0a6}
.avatar{position:absolute;left:24px;top:245px;width:54px;height:54px;border-radius:50%;background:linear-gradient(135deg,#c9b9a6,#7a8aa0)}
.person{position:absolute;left:98px;top:248px}
.person .name{font-family:"Montserrat",sans-serif;font-weight:700;font-size:18px;color:var(--ink)}
.person .loc{font-size:14px;color:var(--ink);margin-top:2px}
.circle-btn{width:38px;height:38px;border-radius:50%;display:flex;align-items:center;justify-content:center}

/* footer */
.footer-brand{left:0;width:1200px;top:3527px;text-align:center;color:var(--white);font-family:"Montserrat",sans-serif;font-weight:500;line-height:1.1}
.footer-brand .l1{display:block;font-size:48px;letter-spacing:22px;padding-left:22px}
.footer-brand .l2{display:block;font-size:46px;letter-spacing:11px;padding-left:11px}
.footer-nav a{position:absolute;top:3664px;color:var(--white);font-size:16px;text-decoration:none;transform:translateX(-50%);white-space:nowrap;font-family:"Poppins",sans-serif}
.contact-icon{top:3739px;width:49px;height:49px;background:var(--yellow);display:flex;align-items:center;justify-content:center}
.contact-text{top:3751px;color:var(--white);font-size:17px}
.copyright{left:0;width:1200px;top:3841px;text-align:center;color:var(--white);font-size:16px}
.copyright span{color:var(--yellow)}
</style>
</head>
<body>

<!-- Header -->
<div class="abs brand"><span class="l1">CREST</span><span class="l2">ELECTRIC</span></div>
<div class="abs topbar"></div>
<div class="abs topbar-item" style="left:461px">
  <svg width="18" height="14" viewBox="0 0 18 14"><rect x="0" y="0" width="18" height="14" rx="2" fill="#fff"/><path d="M1 1l8 6 8-6" stroke="#0d3d8c" stroke-width="1.6" fill="none"/></svg>
  hello@crestwiring.com
</div>
<div class="abs topbar-item" style="left:700px">
  <svg width="15" height="15" viewBox="0 0 24 24"><path fill="#fff" d="M6.6 10.8a15.2 15.2 0 0 0 6.6 6.6l2.2-2.2a1 1 0 0 1 1-.25 11.4 11.4 0 0 0 3.6.57 1 1 0 0 1 1 1V20a1 1 0 0 1-1 1A17 17 0 0 1 3 4a1 1 0 0 1 1-1h3.5a1 1 0 0 1 1 1c0 1.25.2 2.45.57 3.57a1 1 0 0 1-.25 1z"/></svg>
  +1 209 555 0148
</div>
<div class="abs login">
  <svg width="12" height="13" viewBox="0 0 12 13"><circle cx="6" cy="3.5" r="3" fill="#f5b400"/><path d="M0 13c0-3.5 2.7-5.5 6-5.5s6 2 6 5.5z" fill="#f5b400"/></svg>
  Login
</div>
<nav class="abs nav" style="left:0;top:60px;width:1200px;height:40px">
  <a class="active" style="left:398px">Home</a>
  <a style="left:484px">About</a>
  <a style="left:569px">Services</a>
  <a style="left:671px">Projects</a>
  <a style="left:773px">Careers</a>
  <a style="left:870px">Capabilities</a>
  <a style="left:1001px">Contact us</a>
</nav>

<!-- Hero -->
<div class="abs hero-photo" role="img" aria-label="Electrician in a hard hat and high-visibility jacket wiring an electrical panel"></div>
<div class="abs hero-shade"></div>
<div class="abs hero-kicker heading">WELCOME TO</div>
<div class="abs hero-title heading"><b>CREST</b> ELECTRIC</div>
<p class="abs hero-text">Lorem ipsum dolor sit amet, consectetur adipiscing elit, sed do eiusmod tempor incididunt ut labore et dolore magna aliqua.</p>
<div class="abs btn btn-yellow" style="left:111px;top:490px;width:152px;height:46px;font-size:15px">Get Started</div>
<svg class="abs" style="left:0;top:580px" width="1200" height="155" viewBox="0 580 1200 155">
  <polygon points="280,735 555,705 625,650 1200,588 1200,735" fill="#f5b400"/>
  <polygon points="0,735 0,732 565,718 635,666 1200,604 1200,735" fill="#fafafa"/>
</svg>

<!-- Stats -->
<div class="abs stat" style="left:194px"><div class="num">2009</div><div class="lbl">YEAR OF FOUNDATION</div></div>
<div class="abs stat-rule" style="left:450px"></div>
<div class="abs stat" style="left:471px"><div class="num">+3500</div><div class="lbl">FINALIZED PROJECTS</div></div>
<div class="abs stat-rule" style="left:719px"></div>
<div class="abs stat" style="left:719px"><div class="num">+2100</div><div class="lbl">CAREER CLIENTS</div></div>
<div class="abs stat-rule" style="left:943px"></div>

<!-- About -->
<div class="abs about-ring"></div>
<div class="abs about-photo" role="img" aria-label="Two engineers in hard hats reviewing a laptop beside rooftop solar panels"></div>
<h2 class="abs section-title about-title"><b>ABOUT CREST</b> ELECTRIC</h2>
<div class="abs about-rule"></div>
<p class="abs about-text">Lorem ipsum dolor sit amet, consectetur adipiscing elit, sed do eiusmod tempor incididunt ut labore et dolore magna aliqua. Ut enim ad minim veniam, quis nostrud exercitation ullamco laboris nisi ut aliquip ex ea commodo consequat. Duis aute irure dolor in reprehenderit in voluptate velit esse cillum dolore eu fugiat nulla pariatur. Excepteur sint occaecat cupidatat non proident, sunt in culpa qui officia deserunt mollit anim id est laborum.Duis aute irure dolor in reprehenderit in voluptate velit esse cillum dolore eu fugiat nulla pariatur.</p>
<div class="abs btn btn-navy" style="left:631px;top:1339px;width:148px;height:46px;font-size:15px">Read More</div>

<!-- Services -->
<svg class="abs services-band" viewBox="0 1420 1200 750" role="img" aria-label="Electrician working on wiring, tinted in warm yellow">
  <defs>
    <linearGradient id="svcGrad" x1="0" y1="0" x2="1" y2="1">
      <stop offset="0" stop-color="#f0b000"/>
      <stop offset="0.5" stop-color="#e6a600"/>
      <stop offset="1" stop-color="#f3b500"/>
    </linearGradient>
  </defs>
  <polygon points="0,1536 1200,1421 1200,2053 0,2168" fill="url(#svcGrad)"/>
</svg>
<h2 class="abs section-title center-title services-title">OUR <b>SERVICES</b></h2>
<div class="abs services-rule"></div>

<div class="abs service-card on-yellow" style="left:98px">
  <div class="service-name">Lorem ipsum dolor</div>
  <p class="service-text">Excepteur sint occaecat cupidatat non proident, sunt in culpa qui officia laborum.Duis aute irure&nbsp; esse cillum dolore eu fugiat nulla pariatur.</p>
  <div class="service-link">Learn More »</div>
</div>
<div class="abs service-card featured on-white" style="left:461px">
  <div class="service-name">Lorem ipsum dolor</div>
  <p class="service-text">Excepteur sint occaecat cupidatat non proident, sunt in culpa qui officia laborum.Duis aute irure&nbsp; esse cillum dolore eu fugiat nulla pariatur.</p>
  <div class="service-link">Learn More »</div>
</div>
<div class="abs service-card on-yellow" style="left:809px">
  <div class="service-name">Lorem ipsum dolor</div>
  <p class="service-text">Excepteur sint occaecat cupidatat non proident, sunt in culpa qui officia laborum.Duis aute irure&nbsp; esse cillum dolore eu fugiat nulla pariatur.</p>
  <div class="service-link">Learn More »</div>
</div>

<div class="abs service-icon" style="left:203px;background:#fff">
  <svg width="44" height="44" viewBox="0 0 44 44" fill="none" stroke="#f5b400" stroke-width="2.2" stroke-linecap="round"><path d="M15 8v8M29 8v8"/><path d="M10 16h24v6a12 12 0 0 1-24 0z"/><path d="M22 34v6"/><path d="M23 19l-3 5h4l-3 5"/></svg>
</div>
<div class="abs service-icon" style="left:565px;background:var(--navy)">
  <svg width="50" height="50" viewBox="0 0 50 50" fill="none" stroke="#fff" stroke-width="2.2" stroke-linecap="round" stroke-linejoin="round"><circle cx="25" cy="25" r="17"/><path d="M27 14l-8 13h7l-3 10 9-14h-7z"/></svg>
</div>
<div class="abs service-icon" style="left:914px;background:#fff">
  <svg width="44" height="44" viewBox="0 0 44 44" fill="none" stroke="#f5b400" stroke-width="2.2" stroke-linejoin="round"><rect x="11" y="6" width="22" height="30" rx="2"/><rect x="15" y="10" width="14" height="14"/><path d="M23 12l-3 6h4l-3 5"/><path d="M15 28h14M15 32h14M16 36v3M28 36v3"/></svg>
</div>

<svg class="abs arrow" style="left:41px;top:1833px" viewBox="0 0 28 28"><path d="M24 14H5M12 6l-8 8 8 8" stroke="#fff" stroke-width="3" fill="none" stroke-linecap="round" stroke-linejoin="round"/></svg>
<svg class="abs arrow" style="left:1131px;top:1833px" viewBox="0 0 28 28"><path d="M4 14h19M16 6l8 8-8 8" stroke="#fff" stroke-width="3" fill="none" stroke-linecap="round" stroke-linejoin="round"/></svg>

<!-- Projects -->
<h2 class="abs section-title center-title projects-title">OUR <b>PROJECTS</b></h2>
<div class="abs projects-rule"></div>
<div class="abs project" style="left:111px;background:linear-gradient(135deg,#d8c0a8 0%,#9fb3c8 45%,#e2873a 75%,#5a6f8a 100%)" role="img" aria-label="Hands testing a circuit breaker board with a multimeter"></div>
<div class="abs project" style="left:446px;background:linear-gradient(160deg,#e8ebef 0%,#c9cfd6 40%,#6b7b95 70%,#e0b12a 100%)" role="img" aria-label="Electrician in a yellow hard hat fitting a ceiling fixture"></div>
<div class="abs project" style="left:780px;background:linear-gradient(120deg,#4f9a3b 0%,#8fa0ad 40%,#dfe3e8 65%,#3e4b5f 100%)" role="img" aria-label="Electrician in a white hard hat wiring a distribution cabinet"></div>
<div class="abs btn btn-navy" style="left:484px;top:2650px;width:231px;height:47px;font-size:15.5px">View More Projects</div>

<!-- Testimonials -->
<div class="abs testi-band" role="img" aria-label="Blue-tinted wiring and switchgear backdrop"></div>
<h2 class="abs section-title center-title testi-title">CLIENTS <b>TESTIMONIALS</b></h2>

<div class="abs testi-card" style="left:106px">
  <div class="stars">★★★★★</div>
  <p class="testi-text">Lorem ipsum dolor sit amet, consectetur adipiscing elit, sed do eiusmod tempor incididunt ut labore et dolore magna aliqua ut enim ad minim veniam, quis nostrud exercitation ullamco.</p>
  <div class="testi-rule"></div>
  <div class="avatar" role="img" aria-label="Client portrait"></div>
  <div class="person"><div class="name">Dana Reyes</div><div class="loc">Florida, United States</div></div>
</div>
<div class="abs testi-card" style="left:443px">
  <div class="stars">★★★★★</div>
  <p class="testi-text">Lorem ipsum dolor sit amet, consectetur adipiscing elit, sed do eiusmod tempor incididunt ut labore et dolore magna aliqua ut enim ad minim veniam, quis nostrud exercitation ullamco.</p>
  <div class="testi-rule"></div>
  <div class="avatar" role="img" aria-label="Client portrait"></div>
  <div class="person"><div class="name">Dana Reyes</div><div class="loc">Florida, United States</div></div>
</div>
<div class="abs testi-card" style="left:779px">
  <div class="stars">★★★★★</div>
  <p class="testi-text">Lorem ipsum dolor sit amet, consectetur adipiscing elit, sed do eiusmod tempor incididunt ut labore et dolore magna aliqua ut enim ad minim veniam, quis nostrud exercitation ullamco.</p>
  <div class="testi-rule"></div>
  <div class="avatar" role="img" aria-label="Client portrait"></div>
  <div class="person"><div class="name">Dana Reyes</div><div class="loc">Florida, United States</div></div>
</div>

<div class="abs circle-btn" style="left:36px;top:3087px;border:2px solid var(--navy);background:#fff">
  <svg width="12" height="12" viewBox="0 0 12 12"><path d="M8 1L3 6l5 5" stroke="#0d3d8c" stroke-width="2" fill="none"/></svg>
</div>
<div class="abs circle-btn" style="left:1125px;top:3087px;background:var(--navy)">
  <svg width="12" height="12" viewBox="0 0 12 12"><path d="M4 1l5 5-5 5" stroke="#fff" stroke-width="2" fill="none"/></svg>
</div>

<!-- Footer -->
<svg class="abs" style="left:0;top:3330px" width="1200" height="585" viewBox="0 3330 1200 585">
  <polygon points="0,3484 560,3440 640,3358 1200,3336 1200,3915 0,3915" fill="#f5b400"/>
  <polygon points="0,3492 575,3462 652,3382 1200,3360 1200,3915 0,3915" fill="#050505"/>
</svg>
<div class="abs footer-brand"><span class="l1">CREST</span><span class="l2">ELECTRIC</span></div>
<nav class="footer-nav">
  <a style="left:217px">Home</a>
  <a style="left:325px">About</a>
  <a style="left:441px">Services</a>
  <a style="left:564px">Projects</a>
  <a style="left:681px">Careers</a>
  <a style="left:817px">Capabilities</a>
  <a style="left:963px">Contact us</a>
</nav>

<div class="abs contact-icon" style="left:146px">
  <svg width="26" height="20" viewBox="0 0 26 20"><rect width="26" height="20" rx="2" fill="#fff"/><path d="M1 2l12 9 12-9" stroke="#f5b400" stroke-width="2" fill="none"/></svg>
</div>
<div class="abs contact-text" style="left:211px">hello@crestwiring.com</div>
<div class="abs contact-icon" style="left:497px">
  <svg width="20" height="26" viewBox="0 0 20 26"><path d="M10 0a10 10 0 0 0-10 10c0 7 10 16 10 16s10-9 10-16A10 10 0 0 0 10 0z" fill="#fff"/><circle cx="10" cy="10" r="3.5" fill="#f5b400"/></svg>
</div>
<div class="abs contact-text" style="left:567px">Crest Electric,United State.</div>
<div class="abs contact-icon" style="left:855px">
  <svg width="22" height="22" viewBox="0 0 24 24"><path fill="#fff" d="M6.6 10.8a15.2 15.2 0 0 0 6.6 6.6l2.2-2.2a1 1 0 0 1 1-.25 11.4 11.4 0 0 0 3.6.57 1 1 0 0 1 1 1V20a1 1 0 0 1-1 1A17 17 0 0 1 3 4a1 1 0 0 1 1-1h3.5a1 1 0 0 1 1 1c0 1.25.2 2.45.57 3.57a1 1 0 0 1-.25 1z"/></svg>
</div>
<div class="abs contact-text" style="left:925px">+1 209 555 0148</div>

<div class="abs copyright">Copyrights@2024.<span>Crest Electric</span>.All Rights Reserved</div>

</body>
</html>
```